Flyer Tally Desk Ledger Kit

Hi
Can you please design me a DL Flyer for: Tally Desk Ledger Kit
Info:
Starting a new Business ?
Want to save on bookkeeping fees for your existing business?

You can now save 1000's off bookkeeping fees by Doing it Yourself.

Using our Bookkeeper software you simply key in the information as you go.

We offer one on one training, backup and support.
We can assist you with BAS Preparation and Payrol Advice.

Add Modules as required:
Point of Sale Module
Jobs Management Module
Website Intergration Module

Fee set up assistance and training.

Lets get the ball rolling: 1300 462 815
www.tldlk.com.au
admin@tldlk.com.au (use the logo thing you made)

Target Market(s)

Small Business

Colors
ec1f27
f04a50
f59296
fcdcdc
ffffff

Requirements
Nice to have
• image/s related to bookkeeping

```html
<!DOCTYPE html>
<html lang="en">
<head>
<meta charset="utf-8">
<title>Tally Desk Ledger Kit – DL Flyer</title>
<link rel="stylesheet" href="https://fonts.googleapis.com/css2?family=Fira+Sans+Condensed:ital,wght@0,600;1,700;1,800&family=Noto+Sans:wght@700&family=Noto+Serif:ital@1&family=Roboto:ital,wght@0,400;0,500;1,500;1,700&display=swap">
<style>
:root{
  --red:#ec1f27;
  --red-soft:#f04a50;
  --pink:#f59296;
  --blush:#fcdcdc;
  --white:#ffffff;
  --ink:#1c1b1e;
  --charcoal:#2a2a2c;
  --grey:#6d6e71;
  --backdrop:#c39a6e;
}
*{box-sizing:border-box;margin:0;padding:0}
html,body{width:1200px;height:1125px;overflow:hidden;background:var(--backdrop)}
.card{position:absolute;overflow:hidden;box-shadow:6px 8px 14px rgba(0,0,0,.35)}
.front{left:158px;top:135px;width:860px;height:405px;background:var(--white)}
.back{left:155px;top:600px;width:863px;height:406px;background:var(--ink)}
.abs{position:absolute}
svg.shapes{position:absolute;left:0;top:0}

/* front */
.portrait{left:0;top:0;width:360px;height:405px;
  background:linear-gradient(90deg,#c9a48c 0%,#e6cfc1 45%,#f6efea 80%,rgba(255,255,255,0) 100%)}
.brand{left:150px;top:42px;font-family:"Roboto",sans-serif;font-weight:500;font-size:36px;color:var(--red);letter-spacing:-.5px}
.tagline{left:252px;top:96px;font-family:"Noto Serif",serif;font-style:italic;font-size:14px;color:var(--grey)}
.headline{right:35px;top:33px;text-align:right;font-family:"Fira Sans Condensed",sans-serif;font-weight:600;font-size:36px;line-height:39px;color:var(--white)}
.rule{left:583px;top:133px;width:242px;height:3px;border-top:1px solid var(--pink);border-bottom:1px solid var(--pink)}
.question{right:35px;top:152px;text-align:right;font-family:"Fira Sans Condensed",sans-serif;font-style:italic;font-weight:700;font-size:29px;line-height:35px;color:var(--white)}
.saving{left:552px;top:290px;font-family:"Noto Serif",serif;font-style:italic;font-size:19px;line-height:24.5px;color:var(--white)}
.bubble{left:274px;top:240px;width:230px;text-align:center;font-family:"Noto Sans",sans-serif;font-weight:700;font-size:20px;line-height:24.5px;color:var(--ink)}

/* back */
.book-scene{left:370px;top:0;width:493px;height:406px;
  background:radial-gradient(ellipse at 60% 10%,#e8c98c 0%,#9c6a45 35%,#4a2a22 70%,#2a1a18 100%)}
.offer{left:40px;top:42px;font-family:"Roboto",sans-serif;font-weight:500;font-size:27px;line-height:33px;color:var(--red-soft)}
.assist{left:40px;top:160px;font-family:"Roboto",sans-serif;font-weight:500;font-size:27px;line-height:33.5px;color:var(--white)}
.cta-band{left:0;top:311px;width:400px;height:95px;background:var(--red);clip-path:polygon(0 0,360px 0,372px 8px,400px 95px,0 95px)}
.cta-lead{left:160px;top:322px;font-family:"Roboto",sans-serif;font-size:18px;color:var(--white);letter-spacing:.3px}
.cta-phone{left:146px;top:343px;font-family:"Roboto",sans-serif;font-weight:500;font-size:35px;color:var(--white)}
.email{left:385px;top:26px;font-family:"Roboto",sans-serif;font-size:15px;color:var(--white);display:flex;align-items:center;gap:6px}
.site{left:618px;top:20px;font-family:"Roboto",sans-serif;font-weight:700;font-size:21px;color:#4a4a4c}
.contact-rule{left:389px;top:58px;width:439px;height:2px;background:var(--red)}
.pill{left:478px;top:75px;width:250px;height:30px;border-radius:15px;background:var(--red);box-shadow:0 2px 4px rgba(0,0,0,.4);
  font-family:"Roboto",sans-serif;font-weight:500;font-size:18px;line-height:30px;text-align:center;color:var(--white)}
.modules{left:400px;top:114px;width:430px;text-align:center;font-family:"Roboto",sans-serif;font-style:italic;font-weight:700;font-size:14.5px;line-height:19.5px;color:var(--white)}
.modules span::before{content:"";display:inline-block;width:10px;height:10px;border-radius:50%;background:var(--red);margin:0 6px 0 8px;vertical-align:-1px}
</style>
</head>
<body>

<section class="card front">
  <div class="abs portrait" role="img" aria-label="Photo of a smiling woman holding papers"></div>
  <svg class="shapes" width="860" height="405" viewBox="0 0 860 405">
    <defs>
      <linearGradient id="redField" x1="0" y1="0" x2="1" y2="1">
        <stop offset="0" stop-color="#d41a22"/><stop offset="1" stop-color="#ec1f27"/>
      </linearGradient>
      <radialGradient id="bubbleFill" cx=".5" cy=".4" r=".6">
        <stop offset="0" stop-color="#ffffff"/><stop offset=".7" stop-color="#f2f2f2"/><stop offset="1" stop-color="#cfcfd1"/>
      </radialGradient>
    </defs>
    <polygon points="608,0 621,0 470,212 457,212" fill="#fcdcdc"/>
    <polygon points="624,0 860,0 860,405 360,405 467,217" fill="url(#redField)"/>
    <polygon points="500,283 800,283 822,328 800,373 500,373" fill="#2a2a2c"/>
    <circle cx="389" cy="308" r="142" fill="#e9e9ea"/>
    <circle cx="389" cy="308" r="130" fill="url(#bubbleFill)"/>
  </svg>
  <div class="abs brand">Tally Desk Ledger Kit</div>
  <div class="abs tagline">It's easy enough to do yourself</div>
  <h1 class="abs headline">STARTING A<br>NEW BUSINESS?</h1>
  <div class="abs rule"></div>
  <p class="abs question">Want to save on<br>bookkeeping fees for<br>your existing business?</p>
  <p class="abs saving">You can now save<br>1000's off bookkeeping fees<br>by Doing it Yourself.</p>
  <p class="abs bubble">Using<br>our Bookkeeper<br>software you simply<br>key in the<br>information as<br>you go.</p>
</section>

<section class="card back">
  <div class="abs book-scene" role="img" aria-label="Photo of an open book on a stack of books"></div>
  <h2 class="abs offer">We offer one on one<br>training, backup<br>and support.</h2>
  <p class="abs assist">We can assist you with<br>BAS Preparation and<br>Payrol Advice.</p>
  <div class="abs cta-band"></div>
  <p class="abs cta-lead">Lets get the ball rolling</p>
  <p class="abs cta-phone">1300 462 815</p>
  <p class="abs email">
    <svg width="20" height="14" viewBox="0 0 20 14"><rect x="1" y="1" width="18" height="12" rx="1.5" fill="#f59296" stroke="#ec1f27"/><polyline points="1,1 10,8 19,1" fill="none" stroke="#ec1f27" stroke-width="1.4"/></svg>
    admin@tldlk.com.au
  </p>
  <p class="abs site">www.tldlk.com.au</p>
  <div class="abs contact-rule"></div>
  <div class="abs pill">Add Modules as required</div>
  <p class="abs modules"><span>Point of Sale Module</span> <span>Jobs Management Module</span><br><span>Website Intergration Module</span></p>
</section>

</body>
</html>
```